Business Card Re-Design...or logo does not look sharp

Hello

We are a start-up and just need someone to help us.

Our colors are: Marlowe Hush pink (yeah I know) and charcoal for the lettering.

I am attaching our logo which needs cleaning up.

We want the JUST the lady ironing on the table (pink) in front, and the background in charcoal. All the business info can be on the back.

Dims on card are 2 x 2''

Also, if you have better ideas....please let us know!

Thanks

Gregory

La Comadre Vapor
4827 Quellbrook Dr Suite B2
El Paso TX 79936
915-555-0148

```html
<!DOCTYPE html>
<html lang="en">
<head>
<meta charset="utf-8">
<title>La Comadre Vapor – Business Card</title>
<link href="https://fonts.googleapis.com/css2?family=Lato:wght@400;700&display=swap" rel="stylesheet">
<style>
  :root {
    --backdrop: #e4e4e4;
    --charcoal: #1b1a1a;
    --blush: #f4d8d6;
    --ink: #1e1e1e;
  }
  * { margin: 0; padding: 0; box-sizing: border-box; }
  html, body {
    width: 1200px;
    height: 787px;
    overflow: hidden;
    background: var(--backdrop);
    font-family: 'Lato', sans-serif;
  }
  .sheet {
    width: 1200px;
    height: 787px;
    display: flex;
    align-items: center;
    justify-content: center;
    gap: 60px;
  }
  .card {
    width: 500px;
    height: 286px;
    position: relative;
    box-shadow: 0 4px 14px rgba(0,0,0,0.18);
  }
  .card--front {
    background: var(--charcoal);
    display: flex;
    flex-direction: column;
    align-items: center;
    justify-content: center;
    gap: 14px;
  }
  .brand-name {
    color: var(--blush);
    font-weight: 700;
    font-size: 20px;
    letter-spacing: 2px;
    text-transform: uppercase;
  }
  .brand-dot {
    width: 14px;
    height: 14px;
    border-radius: 50%;
    background: var(--blush);
  }
  .card--back {
    background: var(--blush);
  }
  .back-disc {
    position: absolute;
    left: 58px;
    top: 50%;
    transform: translateY(-50%);
    width: 120px;
    height: 120px;
    border-radius: 50%;
    background: var(--charcoal);
  }
  .contact {
    position: absolute;
    left: 205px;
    top: 50%;
    transform: translateY(-50%);
    color: var(--ink);
    font-weight: 700;
    font-size: 15px;
    line-height: 1.3;
    text-transform: uppercase;
    letter-spacing: 0.3px;
  }
</style>
</head>
<body>
  <main class="sheet">
    <section class="card card--front" aria-label="Card front">
      <span class="brand-dot"></span>
      <span class="brand-name">La Comadre Vapor</span>
    </section>
    <section class="card card--back" aria-label="Card back">
      <div class="back-disc"></div>
      <address class="contact" style="font-style:normal">
        La Comadre Vapor 4827<br>
        Quellbrook Dr Suite B2 El Paso<br>
        TX 915-555-0148
      </address>
    </section>
  </main>
</body>
</html>
```